Political Mail Out Quintero front and back

Front
Esteban (9th Grade) Quintero!

What's that famous saying?

Show me who your friends are and I'll tell you who you really are!
(show the two guys)

Arturo Benavides is charged with voter fraud by changing voter addresses from across the RGV so they could vote in Edinburg
Back
Did Esteban (9th Grade) Quintero commit voter fraud when he ran for office in 2016?
(insert blurred photo)

Here is a list of people from all over the RGV that voted in Edinburg in the 2016 race.
Here is a break down:

(highlight the number and where they were first registered to vote)

9 People voted in Edinburg who were registered in Donna.
13 People voted in Edinburg who were registered in San Juan
8 People voted in Edinburg who were registered in Pharr
31 People voted in Edinburg who were registered in McAllen
2 People voted in Edinburg who were registered in La Joya
6 People voted in Edinburg who were registered in Edcouch
2 People voted in Edinburg who were registered in Mercedes
2 People voted in Edinburg who were registered in Monte Alto
6 People voted in Edinburg who were registered in Weslaco
1 Person voted in Edinburg who were registered in Penitas
3 People voted in Edinburg who were registered in Alamo
5 People voted in Edinburg who were registered in Elsa
6 People voted in Edinburg who were registered in Mission
1 Person voted in Edinburg who were registered in Alton

Will Esteban (9th Grade) Quintero CHEAT in 2020?

Only time will tell.

Vote Esteban (9th Grade) Quintero OUT of office.

```html
<!DOCTYPE html>
<html lang="en">
<head>
<meta charset="UTF-8">
<title>Quintero Mail Out – Front and Back</title>
<link rel="stylesheet" href="https://fonts.googleapis.com/css2?family=Montserrat:wght@700;800;900&family=Figtree:wght@400;500;700;800&display=swap">
<style>
  :root {
    --navy: #0d2350;
    --navy-deep: #0a1c42;
    --orange: #f7941d;
    --orange-hot: #f26c0d;
    --yellow: #fed100;
    --yellow-soft: #ffe23a;
    --white: #ffffff;
    --stage: #2b2926;
    --head: "Montserrat", Arial, sans-serif;
    --body: "Figtree", Arial, sans-serif;
  }
  * { margin: 0; padding: 0; box-sizing: border-box; }
  html, body { width: 864px; height: 1200px; overflow: hidden; background: var(--stage); }
  .canvas { position: relative; width: 864px; height: 1200px; }

  .card { position: absolute; left: 42px; width: 780px; height: 487px; overflow: hidden; }
  .card--front { top: 84px; background: var(--navy); }
  .card--back { top: 614px; background: var(--white); }
  .card svg.shapes { position: absolute; inset: 0; width: 100%; height: 100%; }

  /* Front */
  .front__headline {
    position: absolute; left: 24px; top: 50px;
    font-family: var(--head); font-weight: 900; color: var(--navy);
    font-size: 40px; line-height: 0.98; letter-spacing: -1.2px; text-transform: uppercase;
  }
  .front__question {
    position: absolute; left: 27px; top: 200px;
    font-family: var(--head); font-weight: 900; color: #0b0b12;
    font-size: 28px; line-height: 0.98; letter-spacing: -0.6px; text-transform: uppercase;
  }
  .front__saying {
    position: absolute; left: 33px; top: 280px;
    font-family: var(--body); font-weight: 500; color: var(--white);
    font-size: 19px; line-height: 1.2;
  }
  .front__charge {
    position: absolute; left: 40px; top: 400px; width: 400px;
    font-family: var(--body); font-weight: 500; color: var(--white);
    font-size: 16.5px; line-height: 1.23;
  }
  .front__name-mark {
    position: absolute; right: 36px; top: 392px; text-align: left;
    font-family: var(--head); font-weight: 800; color: var(--white);
    line-height: 1; text-transform: uppercase;
  }
  .front__name-mark .first { display: block; font-size: 27px; letter-spacing: 0.5px; }
  .front__name-mark .last { display: block; font-size: 40px; letter-spacing: 0.5px; margin-top: 4px; }

  /* Back */
  .back__headline {
    position: absolute; left: 31px; top: 10px;
    font-family: var(--head); font-weight: 900; color: var(--navy);
    font-size: 19.5px; line-height: 1.08; letter-spacing: -0.4px; text-transform: uppercase;
  }
  .back__intro {
    position: absolute; left: 22px; top: 124px; width: 380px;
    font-family: var(--body); font-weight: 500; color: var(--yellow);
    font-size: 13.5px; line-height: 1.2;
  }
  .back__intro strong { font-weight: 800; }
  .tally {
    position: absolute; left: 23px; top: 176px; width: 370px;
    display: grid; grid-template-columns: 187px 180px; grid-auto-flow: column;
    grid-template-rows: repeat(7, 26.8px);
    list-style: none;
    font-family: var(--body); color: var(--white); font-size: 10.6px; line-height: 1.02;
  }
  .tally strong { font-weight: 800; }
  .back__cheat {
    position: absolute; left: 23px; top: 386px;
    font-family: var(--head); font-weight: 900; color: var(--white);
    font-size: 17px; line-height: 1; letter-spacing: -0.4px; text-transform: uppercase;
  }
  .back__tell {
    position: absolute; left: 23px; top: 441px;
    font-family: var(--head); font-weight: 900; color: var(--orange);
    font-size: 21px; letter-spacing: -0.5px; text-transform: uppercase;
  }
  .vote-out {
    position: absolute; left: 292px; top: 369px; width: 123px; height: 105px;
    background: var(--orange); padding: 9px 7px;
    font-family: var(--head); font-weight: 900; color: var(--navy);
    font-size: 14.2px; line-height: 1.06; letter-spacing: -0.3px; text-transform: uppercase;
  }
</style>
</head>
<body>
<main class="canvas">

  <!-- FRONT -->
  <section class="card card--front" aria-label="Mailer front">
    <svg class="shapes" viewBox="0 0 780 487" preserveAspectRatio="none">
      <defs>
        <linearGradient id="photoTones" x1="0" y1="0" x2="1" y2="1">
          <stop offset="0" stop-color="#c98a6e"/>
          <stop offset="0.5" stop-color="#e6e1dc"/>
          <stop offset="1" stop-color="#7f7f80"/>
        </linearGradient>
        <linearGradient id="orangeSweep" x1="0" y1="0" x2="1" y2="0.3">
          <stop offset="0" stop-color="var(--orange-hot)"/>
          <stop offset="0.55" stop-color="var(--orange)"/>
          <stop offset="1" stop-color="#fba02a"/>
        </linearGradient>
      </defs>
      <path role="img" aria-label="Photo of the two men standing together, smiling"
            d="M330,0 L780,0 L780,270 L560,280 C450,250 360,130 330,0 Z" fill="url(#photoTones)" opacity="0.9"/>
      <path d="M0,0 L310,0 C345,130 440,255 570,283 L780,262 L780,292 C640,340 450,382 280,382 C170,382 70,365 0,340 Z" fill="var(--yellow)"/>
      <path d="M0,0 L284,0 C320,130 420,255 560,284 L780,268 L780,285 C640,330 450,372 280,372 C170,372 70,348 0,325 Z" fill="url(#orangeSweep)"/>
    </svg>

    <h1 class="front__headline">Esteban<br>(9th Grade)<br>Quintero!</h1>
    <h2 class="front__question">What's that<br>famous saying?</h2>
    <p class="front__saying">Show me who your friends<br>are and I'll tell you who you really are!</p>
    <p class="front__charge">Arturo Benavides is charged with voter fraud by changing voter addresses from across the RGV so they could vote in Edinburg</p>
    <div class="front__name-mark"><span class="first">Esteban</span><span class="last">Quintero</span></div>
  </section>

  <!-- BACK -->
  <section class="card card--back" aria-label="Mailer back">
    <svg class="shapes" viewBox="0 0 780 487" preserveAspectRatio="none">
      <defs>
        <linearGradient id="headerSweep" x1="0" y1="0" x2="1" y2="0">
          <stop offset="0" stop-color="var(--orange-hot)"/>
          <stop offset="1" stop-color="var(--orange)"/>
        </linearGradient>
      </defs>
      <path d="M412,0 L452,0 L392,487 L370,487 Z" fill="var(--orange-hot)"/>
      <path d="M438,150 L415,487 L372,487 Z" fill="var(--yellow)"/>
      <path d="M0,0 L425,0 L372,487 L0,487 Z" fill="var(--navy)"/>
      <path d="M0,78 C150,100 300,104 420,86 L417,108 C300,108 150,106 0,92 Z" fill="var(--yellow)"/>
      <path d="M0,0 L428,0 L420,82 C300,100 150,98 0,78 Z" fill="url(#headerSweep)"/>
    </svg>

    <h2 class="back__headline">Did Esteban (9th Grade) Quintero<br>commit voter fraud when he<br>ran for office in 2016?</h2>
    <p class="back__intro">Here is a list of people from all over the RGV that voted in Edinburg in the 2016 race. <strong>Here is a break down:</strong></p>

    <ul class="tally">
      <li><strong>9 People</strong> voted in Edinburg who were registered in <strong>Donna.</strong></li>
      <li><strong>13 People</strong> voted in Edinburg who were registered in <strong>San Juan</strong></li>
      <li><strong>8 People</strong> voted in Edinburg who were registered in <strong>Pharr</strong></li>
      <li><strong>31 People</strong> voted in Edinburg who were registered in <strong>McAllen</strong></li>
      <li><strong>2 People</strong> voted in Edinburg who were registered in <strong>La Joya</strong></li>
      <li><strong>6 People</strong> voted in Edinburg who were registered in <strong>Edcouch</strong></li>
      <li><strong>2 People</strong> voted in Edinburg who were registered in <strong>Mercedes</strong></li>
      <li><strong>2 People</strong> voted in Edinburg who were registered in <strong>Monte Alto</strong></li>
      <li><strong>6 People</strong> voted in Edinburg who were registered in <strong>Weslaco</strong></li>
      <li><strong>1 Person</strong> voted in Edinburg who were registered in <strong>Penitas</strong></li>
      <li><strong>3 People</strong> voted in Edinburg who were registered in <strong>Alamo</strong></li>
      <li><strong>5 People</strong> voted in Edinburg who were registered in <strong>Elsa</strong></li>
      <li><strong>6 People</strong> voted in Edinburg who were registered in <strong>Mission</strong></li>
      <li><strong>1 Person</strong> voted in Edinburg who were registered in <strong>Alton</strong></li>
    </ul>

    <p class="back__cheat">Will Esteban (9th Grade)<br>Quintero cheat in 2020?</p>
    <p class="back__tell">Only time will tell.</p>
    <p class="vote-out">Vote Esteban (9th Grade) Quintero out of office.</p>
  </section>

</main>
</body>
</html>
```